Business Card Design

VEGETABLE FARMING OPERATION PRIMARY CROPS SPINACH,SPRING MIX, HEAD LETTUCE, ROMAINE, BRUSSEL SPROUTS, VELVET TOP GREENS BROCCOLI CAULIFLOWER CELERY NEED A Business card THAT REPRESENTS SOME OF THOSE CROPS AY IDEAS WELCOME..

The business is vegetable farming spinach spring mix head lettuce romaine broccoli brussel sprouts celery carrots target audience is potential shippers of products week spring mix spinach harvesting as well. I colors in mind just need a card that's original

Industry/Entity Type

Farming

Contact Information for Business Card

R&K FARMS LLC BRIDGEWOOD FARMS LLC

```html
<!DOCTYPE html>
<html lang="en">
<head>
<meta charset="utf-8">
<title>R&amp;K Farms – Business Card</title>
<link rel="stylesheet" href="https://fonts.googleapis.com/css2?family=Roboto+Condensed:wght@700&family=Roboto:wght@700&display=swap">
<style>
  :root {
    --backdrop: #0d2b2c;
    --card: #ffffff;
    --band: #66bb0e;
    --lime: #9be52a;
    --rule: #4a4a4a;
    --veg-light: #b9e98a;
    --veg-mid: #7fd13b;
  }
  * { box-sizing: border-box; margin: 0; padding: 0; }
  html, body { width: 1200px; height: 877px; overflow: hidden; }
  body { background: var(--backdrop); position: relative; font-family: "Roboto", Arial, sans-serif; }

  .card {
    position: absolute; left: 257px; top: 259px;
    width: 661px; height: 352px;
    background: var(--card); border-radius: 16px; overflow: hidden;
  }
  .card__band {
    position: absolute; left: 0; top: 0; width: 133px; height: 100%;
    background: var(--band); border-radius: 16px;
  }
  .card__names {
    position: absolute; left: 66px; top: 176px;
    transform: translate(-50%, -50%) rotate(-90deg);
    color: #fff; font-family: "Roboto Condensed", "Arial Narrow", sans-serif;
    font-size: 21px; line-height: 30px; letter-spacing: 0.5px;
    text-align: center; white-space: nowrap;
  }
  .card__crops-art {
    position: absolute; left: 160px; top: 10px;
    display: flex; gap: 16px; align-items: center;
  }
  .crop-art { height: 82px; border-radius: 40px; background: radial-gradient(circle at 40% 40%, var(--veg-light), var(--veg-mid)); }
  .crop-art--sprouts { width: 66px; }
  .crop-art--celery { width: 92px; border-radius: 30px; }
  .crop-art--cauliflower { width: 84px; background: radial-gradient(circle at 50% 40%, #f4efe2, #a9d77a); }
  .crop-art--lettuce { width: 104px; }
  .crop-art--broccoli { width: 70px; }

  .card__tagline {
    position: absolute; left: 222px; top: 110px;
    color: var(--lime); font-size: 18px; letter-spacing: 1.1px; white-space: nowrap;
  }
  .card__rule {
    position: absolute; left: 196px; top: 144px; width: 403px; height: 1px; background: var(--rule);
  }
  .card__divider {
    position: absolute; left: 336px; top: 176px; width: 1px; height: 147px; background: var(--rule);
  }
  .crop-list { position: absolute; list-style: none; color: var(--lime); font-size: 19px; letter-spacing: 1px; white-space: nowrap; }
  .crop-list li { position: absolute; left: 0; }
  .crop-list--left { left: 179px; top: 0; }
  .crop-list--right { left: 376px; top: 0; }
</style>
</head>
<body>
  <section class="card" aria-label="R&amp;K Farms business card">
    <div class="card__band">
      <div class="card__names">R&amp;K FARMS LLC<br>BRIDGEWOOD FARMS LLC</div>
    </div>

    <div class="card__crops-art">
      <div class="crop-art crop-art--sprouts" role="img" aria-label="Illustration of brussels sprouts"></div>
      <div class="crop-art crop-art--celery" role="img" aria-label="Illustration of a celery stalk"></div>
      <div class="crop-art crop-art--cauliflower" role="img" aria-label="Illustration of a cauliflower head"></div>
      <div class="crop-art crop-art--lettuce" role="img" aria-label="Illustration of a head of lettuce"></div>
      <div class="crop-art crop-art--broccoli" role="img" aria-label="Illustration of a broccoli floret"></div>
    </div>

    <h1 class="card__tagline">VEGETABLE FARMING OPERATION</h1>
    <div class="card__rule"></div>

    <ul class="crop-list crop-list--left">
      <li style="top:168px">SPINACH</li>
      <li style="top:204px">SPRING MIX</li>
      <li style="top:236px">ROMAINE</li>
      <li style="top:266px">BROCCOLI</li>
      <li style="top:295px">CELERY</li>
    </ul>
    <div class="card__divider"></div>
    <ul class="crop-list crop-list--right">
      <li style="top:178px">VELVET TOP GREENS</li>
      <li style="top:213px">BRUSSEL SPROUTS</li>
      <li style="top:247px">HEAD LETTUCE</li>
      <li style="top:278px">CAULIFLOWER</li>
    </ul>
  </section>
</body>
</html>
```